Women's Online Clothing Boutique Needs Business Cards

I already have a logo that I would like to use. Some of the things that interest me is black business cards, foil embossed logo, glossy embossed logo, leopard print, no yellow font, rounded edges. I even like just a large logo on the front side with all of my information on the back side.

Contact Information for Business Card

https://silverheron.shopvenlo.com/
https://www.pagelink.net/thesilverheronboutique/
https://www.picfeed.net/thesilverheronboutique/
silverheronboutique@mailora.net

Requirements
Must have
• My Logo
Nice to have
• Leopard Print
Should not have
• No Yellow Font

```html
<!DOCTYPE html>
<html lang="en">
<head>
<meta charset="utf-8">
<title>The Silver Heron Boutique – Business Card</title>
<link rel="stylesheet" href="https://fonts.googleapis.com/css2?family=Poppins:wght@400;600&display=swap">
<style>
  :root {
    --backdrop: #2b2b2d;
    --gold: #c39130;
    --ink: #0b0b0b;
    --card-black: #050505;
    --white: #ffffff;
  }
  * { margin: 0; padding: 0; box-sizing: border-box; }
  html, body {
    width: 1200px;
    height: 1189px;
    overflow: hidden;
    background: var(--backdrop);
    font-family: "Poppins", sans-serif;
  }
  .sheet {
    position: relative;
    width: 1200px;
    height: 1189px;
  }
  .card {
    position: absolute;
    left: 180px;
    width: 840px;
    height: 480px;
    border-radius: 36px;
    overflow: hidden;
  }
  .card--front { top: 90px; background: var(--gold); }
  .card--back { top: 619px; background: var(--card-black); }

  /* Front: brand name centred */
  .brand {
    position: absolute;
    text-align: center;
    font-weight: 400;
    line-height: 1.05;
  }
  .card--front .brand {
    left: 0; right: 0; top: 168px;
    color: var(--ink);
    font-size: 62px;
  }
  .brand__rule {
    position: absolute;
    height: 1.5px;
  }
  .card--front .brand__rule {
    left: 170px; right: 170px; top: 316px;
    background: var(--ink);
  }

  /* Back: brand, person, contacts */
  .card--back .brand {
    right: 60px; top: 48px;
    color: var(--gold);
    font-size: 42px;
    text-align: right;
  }
  .card--back .brand__rule {
    right: 40px; width: 430px; top: 150px;
    background: var(--gold);
  }
  .person {
    position: absolute;
    left: 370px; top: 198px;
  }
  .person__name {
    color: var(--white);
    font-weight: 600;
    font-size: 30px;
    letter-spacing: 3px;
  }
  .person__role {
    color: var(--gold);
    font-size: 17px;
    letter-spacing: 5px;
  }
  .contacts {
    position: absolute;
    left: 370px; top: 300px;
    list-style: none;
  }
  .contact {
    display: flex;
    align-items: center;
    gap: 14px;
    height: 38px;
    color: var(--white);
    font-size: 21px;
  }
  .contact__icon {
    width: 26px; height: 26px;
    flex: none;
    background: var(--gold);
    border-radius: 3px;
    display: flex;
    align-items: center;
    justify-content: center;
  }
</style>
</head>
<body>
<main class="sheet">

  <section class="card card--front" aria-label="Business card front">
    <p class="brand">The Silver Heron<br>Boutique</p>
    <div class="brand__rule"></div>
  </section>

  <section class="card card--back" aria-label="Business card back">
    <p class="brand">The Silver Heron<br>Boutique</p>
    <div class="brand__rule"></div>

    <div class="person">
      <p class="person__name">DANA WHITLOW</p>
      <p class="person__role">DIRECTOR</p>
    </div>

    <ul class="contacts">
      <li class="contact">
        <span class="contact__icon">
          <svg width="18" height="14" viewBox="0 0 18 14" aria-hidden="true">
            <rect x="1" y="1" width="16" height="12" fill="none" stroke="#050505" stroke-width="1.6"/>
            <path d="M1 1 L9 8 L17 1" fill="none" stroke="#050505" stroke-width="1.6"/>
          </svg>
        </span>
        silverheronboutique@mailora.net
      </li>
      <li class="contact">
        <span class="contact__icon" aria-hidden="true"></span>
        thesilverheronboutique/
      </li>
      <li class="contact">
        <span class="contact__icon" aria-hidden="true"></span>
        thesilverheronboutique/
      </li>
      <li class="contact">
        <span class="contact__icon">
          <svg width="18" height="18" viewBox="0 0 18 18" aria-hidden="true">
            <circle cx="9" cy="9" r="7.5" fill="none" stroke="#050505" stroke-width="1.4"/>
            <ellipse cx="9" cy="9" rx="3.5" ry="7.5" fill="none" stroke="#050505" stroke-width="1.2"/>
            <path d="M1.5 9 H16.5 M3 5 H15 M3 13 H15" stroke="#050505" stroke-width="1.1"/>
          </svg>
        </span>
        silverheron.shopvenlo.com
      </li>
    </ul>
  </section>

</main>
</body>
</html>
```